Therapist website

I need a sqaure space web design for my therapy practice. I need a home page, a services page with 4 subpages, an about me, an insurnace page, a contact page, an EMDR page

```html
<!DOCTYPE html>
<html lang="en">
<head>
<meta charset="utf-8">
<title>Willowcreek Family Counseling</title>
<link rel="stylesheet" href="https://fonts.googleapis.com/css2?family=Lato:wght@300;400;700;900&family=Oswald:wght@500&family=Great+Vibes&display=swap">
<style>
:root{
  --teal:#3bbdc3;
  --teal-dark:#1a9a9f;
  --teal-deep:#13878c;
  --teal-light:#83d0d5;
  --teal-pale:#c9ecee;
  --nav:#8bd3d7;
  --ink:#333;
  --grey-bg:#f4f4f4;
  --footer:#a9a9a9;
  --footer-bar:#616161;
  --white:#fff;
}
*{box-sizing:border-box;margin:0;padding:0}
html,body{width:1200px;height:2922px;overflow:hidden}
body{font-family:'Lato',sans-serif;color:var(--ink);background:var(--grey-bg);position:relative}
.btn{position:absolute;display:flex;align-items:center;justify-content:center;background:var(--teal);color:var(--white);font-weight:700;font-size:15px;border-radius:20px;text-transform:uppercase}
.read-more{position:absolute;width:140px;height:33px;border-radius:17px;background:var(--teal);color:var(--white);font-size:11px;font-weight:700;display:flex;align-items:center;padding-left:24px;text-transform:uppercase}
.read-more::after{content:"›";position:absolute;right:5px;top:5px;width:23px;height:23px;border-radius:50%;background:var(--white);color:var(--teal);font-size:20px;line-height:20px;text-align:center}
.read-more.light{background:var(--white);color:var(--teal)}
.read-more.light::after{background:var(--teal);color:var(--white)}
.section-title{position:absolute;color:var(--teal);font-size:25px;font-weight:400;text-transform:uppercase;border-bottom:2px solid var(--teal);padding-bottom:2px;white-space:nowrap}

/* header */
.header{position:absolute;left:0;top:0;width:1200px;height:136px;background:var(--grey-bg)}
.brand{position:absolute;left:62px;top:40px;display:flex;align-items:center;gap:10px}
.brand-dot{width:34px;height:34px;border-radius:50%;background:var(--teal)}
.brand-name{font-weight:900;font-size:25px;color:#2a2a2a;letter-spacing:1px}
.brand-sub{position:absolute;left:106px;top:78px;font-size:10px;letter-spacing:2px;color:var(--teal-dark)}
.phone-tab{position:absolute;left:925px;top:0;width:275px;height:47px;background:var(--teal-dark);border-radius:0 0 0 24px;color:var(--white);font-size:23px;font-weight:700;display:flex;align-items:center;justify-content:center;gap:10px}
.follow{position:absolute;left:975px;top:58px;width:140px;text-align:center;color:var(--teal);font-weight:700;font-size:17px}
.social{position:absolute;display:flex;gap:5px}
.social span{width:22px;height:22px;border-radius:50%;background:#bdbdbd}
.nav{position:absolute;left:0;top:136px;width:1200px;height:36px;background:var(--nav)}
.nav a{position:absolute;top:0;height:36px;line-height:36px;text-align:center;color:var(--white);font-size:16px;text-decoration:none;border-right:1px solid rgba(255,255,255,.6)}
.nav a.active{background:var(--teal-dark)}
.nav-cta{position:absolute;left:937px;top:130px;width:197px;height:46px;background:var(--teal-deep);color:var(--white);font-weight:700;font-size:14px;line-height:16px;text-align:center;padding-top:7px;text-transform:uppercase}

/* hero */
.hero{position:absolute;left:0;top:172px;width:1200px;height:608px;background:linear-gradient(100deg,#5fb6bb 0%,#4aa9ae 40%,#6cc2c6 70%,#3fa3a9 100%)}
.hero-title{position:absolute;left:497px;top:526px;font-family:'Oswald',sans-serif;font-weight:500;color:var(--white);font-size:58px;line-height:1;letter-spacing:-1px;white-space:nowrap}
.hero-script{position:absolute;left:565px;top:596px;font-family:'Great Vibes',cursive;color:var(--white);font-size:66px;line-height:1;word-spacing:8px;white-space:nowrap}
.hero-btn{left:696px;top:678px;width:216px;height:47px;border-radius:4px;background:var(--teal-dark);font-size:15px}

/* about */
.about-text{position:absolute;left:74px;top:922px;width:578px;font-size:14.3px;line-height:21.5px;text-align:justify}
.form-box{position:absolute;left:709px;top:859px;width:415px;height:296px;border:2px solid var(--teal-light)}
.form-tab{position:absolute;left:740px;top:843px;width:300px;height:45px;background:var(--teal);color:var(--white);font-size:18px;line-height:45px;text-align:center;text-transform:uppercase;white-space:nowrap}
.field{position:absolute;left:744px;width:343px;background:var(--teal-pale);border:1px solid var(--teal-light);border-radius:3px;color:#666;font-size:17px;padding:8px 18px}
.field b{color:var(--teal);font-weight:400}
.submit{left:842px;top:1099px;width:138px;height:35px;border-radius:18px}

/* emdr */
.emdr{position:absolute;left:0;top:1228px;width:1200px;height:303px;background:var(--teal-light)}
.emdr-img{position:absolute;left:78px;top:1274px;width:331px;height:216px;border:5px solid var(--teal-deep);background:linear-gradient(135deg,#e2b9a0 0%,#cf9878 55%,#b87a5c 100%)}
.emdr-title{color:var(--white);border-color:var(--white);left:444px;top:1288px}
.emdr-text{position:absolute;left:444px;top:1342px;width:680px;color:var(--white);font-size:13.4px;line-height:18.5px}

/* services */
.services{position:absolute;left:0;top:1531px;width:1200px;height:364px;background:var(--white)}
.svc{position:absolute;top:1686px;width:320px;text-align:center}
.svc h3{color:var(--teal);font-size:13px;font-weight:700;text-transform:uppercase;margin-bottom:3px}
.svc p{font-size:11.5px;font-weight:700;line-height:15px;color:#333;padding:0 26px}
.svc-div{position:absolute;top:1680px;width:1px;height:185px;background:var(--teal-light)}

/* testimonials */
.testi{position:absolute;left:0;top:1895px;width:1200px;height:540px;background:var(--teal-light)}
.avatar{position:absolute;top:2055px;width:140px;height:140px;border-radius:50%;border:4px solid var(--teal-deep)}
.quote{position:absolute;top:2224px;width:330px;text-align:center;color:var(--white);font-size:14.5px;line-height:19px}
.name{position:absolute;top:2345px;width:330px;text-align:center;color:#2a2a2a;font-weight:700;font-size:18px;text-transform:uppercase}
.arrow{position:absolute;top:2170px;color:var(--white);font-size:46px;font-weight:700}

/* cta */
.cta-text{position:absolute;left:150px;top:2480px;width:610px;text-align:center;color:var(--teal-dark);font-size:25px;line-height:30px;text-transform:uppercase}
.cta-text span{border-bottom:2px solid var(--teal-dark)}
.cta-btn{left:773px;top:2482px;width:230px;height:54px;border-radius:4px;background:var(--teal-light);font-weight:400;font-size:19px;line-height:20px;text-align:center}

/* footer */
.footer{position:absolute;left:0;top:2587px;width:1200px;height:275px;background:var(--footer);color:var(--white)}
.foot-brand{position:absolute;left:74px;top:2665px;display:flex;align-items:center;gap:8px;font-weight:900;font-size:23px;letter-spacing:1px;color:var(--white)}
.foot-brand i{width:30px;height:30px;border-radius:50%;background:var(--white)}
.foot-sub{position:absolute;left:112px;top:2699px;font-size:10px;letter-spacing:2px;color:var(--white)}
.foot-about{position:absolute;left:74px;top:2752px;width:260px;font-size:11.5px;line-height:14px;text-align:justify;color:var(--white)}
.foot-div{position:absolute;top:2633px;width:1px;height:200px;background:rgba(255,255,255,.7)}
.foot-h{position:absolute;top:2626px;font-size:21px;font-weight:700;text-transform:uppercase;padding-bottom:6px;border-bottom:1px solid rgba(255,255,255,.5);color:var(--white)}
.links{position:absolute;left:436px;top:2680px;list-style:none;font-size:16px;line-height:23px;color:var(--white)}
.links li::before{content:"‹";margin-right:12px}
.contact{position:absolute;left:678px;top:2680px;font-size:13px;line-height:22px;color:var(--white)}
.contact .row{display:flex;align-items:center;gap:9px}
.contact svg{width:12px;height:12px;fill:var(--white)}
.foot-social{position:absolute;left:960px;top:2689px;display:flex;gap:3px}
.foot-social span{width:26px;height:26px;border-radius:50%;background:var(--white)}
.call{position:absolute;left:958px;top:2755px;font-size:22px;font-weight:700;line-height:27px;text-transform:uppercase;border-top:1px solid rgba(255,255,255,.6);padding-top:14px;width:160px;color:var(--white)}
.foot-bar{position:absolute;left:0;top:2862px;width:1200px;height:60px;background:var(--footer-bar);color:#ddd;font-size:15px;text-align:center;line-height:60px}
</style>
</head>
<body>

<header class="header">
  <div class="brand"><span class="brand-dot"></span><span class="brand-name">WILLOWCREEK</span></div>
  <div class="brand-sub">FAMILY COUNSELING</div>
  <div class="phone-tab">
    <svg width="20" height="20" viewBox="0 0 24 24" fill="#fff"><path d="M6.6 10.8a15 15 0 0 0 6.6 6.6l2.2-2.2c.3-.3.7-.4 1-.2 1.1.4 2.3.6 3.6.6.6 0 1 .4 1 1V20c0 .6-.4 1-1 1A17 17 0 0 1 3 4c0-.6.4-1 1-1h3.5c.6 0 1 .4 1 1 0 1.3.2 2.5.6 3.6.1.3 0 .7-.2 1z"/></svg>
    555-204-7731
  </div>
  <div class="follow">Follow Us</div>
  <div class="social" style="left:975px;top:86px"><span></span><span></span><span></span><span></span><span></span></div>
</header>

<nav class="nav">
  <a class="active" href="#" style="left:66px;width:105px">Home</a>
  <a href="#" style="left:171px;width:155px">About me</a>
  <a href="#" style="left:326px;width:140px">Services</a>
  <a href="#" style="left:466px;width:125px">EMDR</a>
  <a href="#" style="left:591px;width:155px">Insurance</a>
  <a href="#" style="left:746px;width:143px">Contact</a>
</nav>
<div class="nav-cta">Schedule your<br>appointment</div>

<section class="hero" role="img" aria-label="Smiling family of four embracing outdoors, tinted teal"></section>
<div class="hero-title">Family Counseling Sessions</div>
<div class="hero-script">Work With Me</div>
<div class="btn hero-btn">Make Appointment</div>

<h2 class="section-title" style="left:74px;top:858px">About me</h2>
<p class="about-text">Lorem ipsum dolor sit amet, consectetuer adipiscing elit. Aenean commodo ligula eget dolor. Aenean massa. Cum sociis natoque penatibus et magnis dis parturient montes, nascetur ridiculus mus. Donec quam felis, ultricies nec, pellentesque eu, pretium quis, sem. Nulla consequat massa quis enim. Donec pede justo, fringilla vel, aliquet nec, vulputate eget, arcu. In enim justo, rhoncus ut, imperdiet a, venenatis vitae, justo. Nullam dictum felis eu pede mollis pretium. Integer tincidunt. Cras dapibus. Vivamus elementum semper nisi. Aenean vulputate eleifend tellus. Aenean leo ligula, porttitor eu, blandit vel Cras dapibus. Vivamus elementum semper nisi.</p>
<div class="read-more" style="left:74px;top:1120px">Read more</div>

<div class="form-box"></div>
<div class="form-tab">Schdule your appointment</div>
<div class="field" style="top:908px;height:39px">Name<b>*</b></div>
<div class="field" style="top:955px;height:39px">Email <b>*</b></div>
<div class="field" style="top:1001px;height:84px">Message<b>*</b></div>
<div class="btn submit">Submit</div>

<section class="emdr"></section>
<div class="emdr-img" role="img" aria-label="Close-up photograph of a human eye"></div>
<h2 class="section-title emdr-title">EMDR</h2>
<p class="emdr-text">Lorem ipsum dolor sit amet, consectetur adipiscing elit. Quid autem habent admirationis, cum prope accesseris? An hoc usque quaque, aliter in vita? Non igitur de improbo, sed de callido improbo quaerimus, qualis Q. Nam quibus rebus efficiuntur voluptates, eae non sunt in potestate sapientis. Negare non possum. Huic mori optimum esse propter desperationem sapientiae, illi propter spem vivere. Quid enim me prohiberet Epicureum esse.</p>
<div class="read-more light" style="left:440px;top:1459px">Read more</div>

<section class="services"></section>
<h2 class="section-title" style="left:530px;top:1600px">Services</h2>
<div class="svc" style="left:43px"><h3>Stress Management</h3><p>Lorem ipsum dolor sit amet, consectetur adipiscing elit. Quid autem habent admirationis, cum prope accesseris? An hoc</p></div>
<div class="svc-div" style="left:397px"></div>
<div class="svc" style="left:440px"><h3>Personal Coaching</h3><p>Lorem ipsum dolor sit amet, consectetur adipiscing elit. Quid autem habent admirationis, cum prope accesseris? An hoc</p></div>
<div class="svc-div" style="left:799px"></div>
<div class="svc" style="left:837px"><h3>Yoga</h3><p>Lorem ipsum dolor sit amet, consectetur adipiscing elit. Quid autem habent admirationis, cum prope accesseris? An hoc</p></div>
<div class="read-more" style="left:133px;top:1771px">Read more</div>
<div class="read-more" style="left:530px;top:1771px">Read more</div>
<div class="read-more" style="left:935px;top:1771px">Read more</div>

<section class="testi"></section>
<h2 class="section-title" style="left:510px;top:1968px;color:var(--white);border-color:var(--white)">Testimonials</h2>
<div class="arrow" style="left:32px">‹</div>
<div class="arrow" style="left:1130px">›</div>
<div class="avatar" style="left:160px;background:linear-gradient(160deg,#d8b7a0,#9a5c3e)" role="img" aria-label="Portrait of a client"></div>
<div class="avatar" style="left:530px;background:linear-gradient(160deg,#c9cdd2,#4b3a30)" role="img" aria-label="Portrait of a client"></div>
<div class="avatar" style="left:896px;background:linear-gradient(160deg,#b7b9bb,#6a4d3e)" role="img" aria-label="Portrait of a client"></div>
<p class="quote" style="left:65px">❝ After having a baby, it was hard for me to lose the cellulite on my thighs. After a few treatments I started seeing amazing results. Now I can wear a bathing suit again, and I feel more confident! ❞</p>
<p class="quote" style="left:435px">❝ At first this sounded too good to be true, but after 6 sessions I was down over 6 inches! I can't believe the amazing results I've seen in such a short time. Sculpt Glow has helped with those areas that diet &amp; exercise couldn't. ❞</p>
<p class="quote" style="left:801px">❝ The BrightWave treatments are extremely effective! I have lost a total of 17 inches, and this has given me such motivation to continue down the path of eating well and exercising. I cannot say enough &amp; confidence. ❞</p>
<div class="name" style="left:65px">Marla</div>
<div class="name" style="left:435px">Teodoro</div>
<div class="name" style="left:801px">Everett</div>

<div class="cta-text"><span>Schedule your appointment today &amp;</span><br><span>start family counseling sessions</span></div>
<div class="btn cta-btn">Schedule your<br>appointment</div>

<footer class="footer"></footer>
<div class="foot-brand"><i></i>WILLOWCREEK</div>
<div class="foot-sub">FAMILY COUNSELING</div>
<p class="foot-about">Lorem ipsum dolor sit amet, consectetur adipiscing elit. Quid autem habent admirationis, cum prope accesseris? An hoc usque quaque, aliter in vita? Non igitur de improbo.</p>
<div class="foot-div" style="left:384px"></div>
<div class="foot-div" style="left:627px"></div>
<div class="foot-div" style="left:902px"></div>
<div class="foot-h" style="left:436px;width:145px">Quick Links</div>
<ul class="links"><li>Home</li><li>About me</li><li>Services</li><li>EMDR</li><li>Insurance</li><li>Contact</li></ul>
<div class="foot-h" style="left:678px;width:176px">Contact</div>
<div class="contact">
  <div>4270 Linden Park Rd<br>Maple Falls, IL 60412</div>
  <div class="row"><svg viewBox="0 0 24 24"><path d="M6.6 10.8a15 15 0 0 0 6.6 6.6l2.2-2.2c.3-.3.7-.4 1-.2 1.1.4 2.3.6 3.6.6.6 0 1 .4 1 1V20c0 .6-.4 1-1 1A17 17 0 0 1 3 4c0-.6.4-1 1-1h3.5c.6 0 1 .4 1 1 0 1.3.2 2.5.6 3.6.1.3 0 .7-.2 1z"/></svg>555-204-7731</div>
  <div class="row"><svg viewBox="0 0 24 24"><rect x="6" y="2" width="12" height="20" rx="2"/></svg>555-204-7795</div>
  <div class="row"><svg viewBox="0 0 24 24"><path d="M2 5h20v14H2z"/></svg>hello@willowcreekfc.com</div>
  <div class="row"><svg viewBox="0 0 24 24"><circle cx="12" cy="12" r="10"/></svg>www.willowcreekfc.com</div>
</div>
<div class="foot-h" style="left:954px;border:none">Follow us on</div>
<div class="foot-social"><span></span><span></span><span></span><span></span><span></span></div>
<div class="call">Call us on<br>555-204-7731</div>
<div class="foot-bar">© 2018 Willowcreek &nbsp;|&nbsp; Privacy Policy &nbsp;|&nbsp; User Agreement</div>

</body>
</html>
```